Website Design for Spatial Humanities Non-Profit: Civic Landmark Atlas

We seek a Wordpress website template for Civic Landmark Atlas (CLA) a 501(c)(3) non-profit in the emergent field of spatial humanities dedicated to digitally preserving global historic and cultural sites. A unique collaboration between individuals in diverse disciplines (academia, technology, arts, and social entrepreneurship), CLA melds age-old scholarship with 21st Century technology to assert the importance of physical location to the understanding of history. This actualized focus allows for a more comprehensive, interactive, and “living” reconstruction of the past than previously thought possible.
CLA, through its own initiatives as well as those of others to whom it provides services, has created a prototype for digital preservation applicable to every country, culture, and subject matter. The organization is
• Pioneering new technology and multimedia techniques for documenting historic and cultural sites;
• Leading international field expeditions to geo-locate and digitize sites, as well as record eyewitness testimony; and
• Transforming research data into dynamically new educational applications.
The template should have a distinctive homepage, themed pages (about, news, projects, opportunities), and no blog elements (e.g., comment section). Admin friendliness is a plus.
We have posted separately for a logo design, which will perhaps feature a scattering of pixels horizontally that gradually cohere to form a globe (featuring "CLA") in the center. To participate in that contest see: http://gigs.pixelvaultwork.com/gig.aspx?id=48213
Non-Profit

```html
<!DOCTYPE html>
<html lang="en">
<head>
<meta charset="utf-8">
<title>Civic Landmark Atlas</title>
<link rel="stylesheet" href="https://fonts.googleapis.com/css2?family=Molengo&family=Andada+Pro:wght@400&family=PT+Sans:wght@400&family=PT+Sans+Narrow:wght@400&display=swap">
<style>
:root{
  --header-top:#f1efc9;
  --header-bottom:#dcd9a6;
  --hero:#b9b78c;
  --hero-dark:#a9a77c;
  --band-light:#d9d7a6;
  --band-dark:#a2a27c;
  --ink:#2f2f22;
  --ink-soft:#4a4a36;
  --hero-text:#f6f4dc;
  --rule:#8e8c66;
  --button:#2b2b26;
  --button-text:#f1f1ea;
  --footer:#121410;
  --footer-text:#e6e6dc;
  --footer-rule:#2a2c26;
  --bullet:#b8b98a;
}
*{box-sizing:border-box;margin:0;padding:0}
html,body{width:709px;height:1200px;overflow:hidden}
body{position:relative;background:var(--band-light);color:var(--ink);font-family:"Andada Pro",Georgia,serif}
.abs{position:absolute}
.heading{font-family:"Molengo",sans-serif;font-weight:400}

/* header */
.site-header{left:0;top:0;width:709px;height:57px;background:linear-gradient(var(--header-top),var(--header-bottom));border-bottom:1px solid #c9c696}
.brand{left:30px;top:15px;width:110px;text-align:center;color:var(--ink-soft);font-family:"PT Sans",sans-serif}
.brand-mark{font-size:20px;line-height:20px}
.brand-name{font-size:10px;line-height:12px;white-space:nowrap}
.nav-item{top:0;height:57px;border-left:1px solid #cfcc9c;padding-top:20px;font-family:"PT Sans",sans-serif;color:var(--ink-soft);white-space:nowrap}
.nav-title{font-size:14px;line-height:14px;letter-spacing:-.2px}
.nav-sub{font-size:7.5px;letter-spacing:.6px;line-height:10px;text-transform:uppercase}
.nav-arrow{top:22px;width:9px;height:12px;background:#c5c293;border-radius:2px}
.nav-arrow svg{display:block}

/* hero */
.hero{left:0;top:57px;width:709px;height:240px;background:linear-gradient(180deg,var(--hero),var(--hero-dark));border-bottom:1px solid #e6e4bf}
.hero-photo{left:373px;top:82px;width:274px;height:196px;background:linear-gradient(160deg,#8db0a8 0%,#5d6d52 40%,#5c7a35 70%,#8d8468 100%);clip-path:polygon(4% 30%,22% 5%,100% 0,100% 100%,3% 92%,0 60%)}
.hero-title{left:69px;top:78px;font-family:"PT Sans Narrow",sans-serif;font-weight:400;font-size:37px;line-height:40px;color:#555544;text-shadow:0 1px 0 #e9e7c6}
.hero-sub{left:69px;top:118px;font-family:"PT Sans Narrow",sans-serif;font-size:21px;line-height:24px;color:#fbfae8;text-shadow:0 1px 1px #6a6a52;white-space:nowrap}
.hero-copy{left:71px;top:153px;width:296px;font-size:11px;line-height:16.5px;color:var(--hero-text)}

/* features */
.section-title{left:38px;top:315px;font-size:22px;color:var(--ink);text-shadow:0 1px 0 #f0eecc}
.feature{top:358px;width:160px}
.feature-icon{float:left;width:43px;height:43px;margin-right:4px;border-radius:6px}
.feature h3{font-size:17.5px;line-height:20px;letter-spacing:.8px;color:var(--ink-soft);margin-top:8px}
.feature p{font-size:9px;line-height:13px;color:var(--ink)}
.button{display:block;background:linear-gradient(#4a4a44,var(--button));color:var(--button-text);font-family:"PT Sans",sans-serif;font-size:8.5px;text-align:center;border-radius:2px;box-shadow:0 1px 2px rgba(0,0,0,.3)}
.btn-view{top:466px;width:52px;height:16px;line-height:16px}

/* stories */
.stories{left:0;top:508px;width:709px;height:169px;background:var(--band-dark);border-top:1px solid #e5e3c0;border-bottom:1px solid #e5e3c0}
.story-title{top:534px;font-size:17.5px;letter-spacing:.8px;color:#33332a}
.story-thumb{top:555px;width:76px;height:66px;border:2px solid #e7e5cf;box-shadow:0 1px 2px rgba(0,0,0,.3)}
.story-copy{top:563px;width:214px;font-size:8.4px;line-height:12.4px;color:#2a2a20}
.btn-read{width:73px;height:16px;line-height:16px}

/* session */
.session-title{left:38px;top:706px;font-size:13px;letter-spacing:.8px;color:var(--ink)}
.session-copy{left:38px;top:729px;width:160px;font-size:9px;line-height:13.2px;color:var(--ink)}
.gallery-image{width:201px;height:99px;box-shadow:1px 2px 3px rgba(0,0,0,.35)}
.gallery-caption{width:201px;font-size:9.5px;color:var(--ink-soft);border-bottom:1px solid var(--rule);padding-bottom:3px}

/* footer */
.site-footer{left:0;top:1003px;width:709px;height:197px;background:var(--footer)}
.footer-col{top:1021px;width:130px;color:var(--footer-text);font-family:"PT Sans",sans-serif}
.footer-col h4{font-weight:400;font-size:15px;line-height:15px;margin-bottom:8px}
.footer-col.divider{border-right:1px solid var(--footer-rule);height:118px}
.page-links{list-style:none;font-size:11px}
.page-links li{border-top:1px solid var(--footer-rule);height:18px;line-height:18px}
.page-links li:last-child{border-bottom:1px solid var(--footer-rule)}
.bullets{list-style:none;font-family:"Andada Pro",Georgia,serif;font-size:9px;line-height:13px;padding-left:10px}
.bullets li{position:relative;padding-left:3px}
.bullets li::before{content:"";position:absolute;left:-9px;top:4px;border-left:4px solid var(--bullet);border-top:3px solid transparent;border-bottom:3px solid transparent}
.contact{font-family:"Andada Pro",Georgia,serif;font-size:9px;line-height:13.5px;padding-left:7px}
.footer-brand{right:44px;top:1157px;text-align:right;color:var(--footer-text);font-family:"PT Sans",sans-serif}
.footer-brand .name{font-size:17px;line-height:19px}
.footer-brand .rights{font-size:9px;line-height:11px}
</style>
</head>
<body>

<header class="site-header abs">
  <div class="brand abs">
    <div class="brand-mark">CLA</div>
    <div class="brand-name">Civic Landmark Atlas</div>
  </div>
  <nav>
    <div class="nav-item abs" style="left:142px;width:88px;border-left:none;padding-left:5px"><div class="nav-title">Home Page</div><div class="nav-sub">Start here</div></div>
    <div class="nav-arrow abs" style="left:218px"><svg width="9" height="12"><path d="M2 3l2.5 2.5L7 3M2 7l2.5 2.5L7 7" fill="none" stroke="#555" stroke-width="1"/></svg></div>
    <div class="nav-item abs" style="left:230px;width:80px;padding-left:10px"><div class="nav-title">About us</div><div class="nav-sub">CLA</div></div>
    <div class="nav-arrow abs" style="left:299px"><svg width="9" height="12"><path d="M2 3l2.5 2.5L7 3M2 7l2.5 2.5L7 7" fill="none" stroke="#555" stroke-width="1"/></svg></div>
    <div class="nav-item abs" style="left:311px;width:92px;padding-left:8px"><div class="nav-title">Technology</div><div class="nav-sub">Pioneering</div></div>
    <div class="nav-arrow abs" style="left:391px"><svg width="9" height="12"><path d="M2 3l2.5 2.5L7 3M2 7l2.5 2.5L7 7" fill="none" stroke="#555" stroke-width="1"/></svg></div>
    <div class="nav-item abs" style="left:404px;width:85px;padding-left:11px"><div class="nav-title">Research</div><div class="nav-sub">Non-profit</div></div>
    <div class="nav-arrow abs" style="left:478px"><svg width="9" height="12"><path d="M2 3l2.5 2.5L7 3M2 7l2.5 2.5L7 7" fill="none" stroke="#555" stroke-width="1"/></svg></div>
    <div class="nav-item abs" style="left:490px;width:83px;padding-left:7px"><div class="nav-title">Initiatives</div><div class="nav-sub">Projects</div></div>
    <div class="nav-arrow abs" style="left:562px"><svg width="9" height="12"><path d="M2 3l2.5 2.5L7 3M2 7l2.5 2.5L7 7" fill="none" stroke="#555" stroke-width="1"/></svg></div>
    <div class="nav-item abs" style="left:573px;width:84px;padding-left:7px;border-right:1px solid #cfcc9c"><div class="nav-title">Contribute</div><div class="nav-sub">Help CLA</div></div>
    <div class="nav-arrow abs" style="left:645px"><svg width="9" height="12"><path d="M2 3l2.5 2.5L7 3M2 7l2.5 2.5L7 7" fill="none" stroke="#555" stroke-width="1"/></svg></div>
  </nav>
</header>

<section class="hero abs"></section>
<div class="hero-photo abs" role="img" aria-label="Photo of mountain ruins with terraced ancient stonework"></div>
<h1 class="hero-title abs">Civic Landmark Atlas</h1>
<p class="hero-sub abs">Documenting historical and cultural sites</p>
<p class="hero-copy abs">Vivamus feugiat hendrerit diam non posuere. Nunc ligula libero, suscipit eu fermentum sit amet, adipiscing ut ipsum. Sed venenatis lacinia tellus eu malesuada. Sed cursus feugiat massa vitae auctor. Morbi interdum vestibulum eros, at rutrum enim ullamcorper in. Vestibulum lectus leo, rhoncus at rhoncus sit amet, semper id massa.</p>

<h2 class="section-title heading abs">Civic Landmark Atlas H1 Header</h2>

<div class="feature abs" style="left:37px">
  <div class="feature-icon" role="img" aria-label="Lifebuoy icon" style="background:#d9604a"></div>
  <h3 class="heading">Description</h3>
  <p>Ut ut tellus augue, ut rhoncus massa. Donec nisl nulla, molestie a semper in, luctus ac nunc. Cras eget nibh eu eros sollicitudin imperdiet.</p>
</div>
<div class="feature abs" style="left:199px">
  <div class="feature-icon" role="img" aria-label="Padlock icon" style="background:#9c9c94"></div>
  <h3 class="heading">Description</h3>
  <p>Ut ut tellus augue, ut rhoncus massa. Donec nisl nulla, molestie a semper in, luctus ac nunc. Cras eget nibh eu eros sollicitudin imperdiet.</p>
</div>
<div class="feature abs" style="left:359px">
  <div class="feature-icon" role="img" aria-label="Star icon" style="background:#efa52a"></div>
  <h3 class="heading">Description</h3>
  <p>Ut ut tellus augue, ut rhoncus massa. Donec nisl nulla, molestie a semper in, luctus ac nunc. Cras eget nibh eu eros sollicitudin imperdiet.</p>
</div>
<div class="feature abs" style="left:518px">
  <div class="feature-icon" role="img" aria-label="Notepad and pencil icon" style="background:#b8b8b0"></div>
  <h3 class="heading">Description</h3>
  <p>Ut ut tellus augue, ut rhoncus massa. Donec nisl nulla, molestie a semper in, luctus ac nunc. Cras eget nibh eu eros sollicitudin imperdiet.</p>
</div>
<a class="button btn-view abs" style="left:40px">view</a>
<a class="button btn-view abs" style="left:200px">view</a>
<a class="button btn-view abs" style="left:360px">view</a>
<a class="button btn-view abs" style="left:519px">view</a>

<section class="stories abs"></section>
<h3 class="story-title heading abs" style="left:38px">Description</h3>
<div class="story-thumb abs" style="left:40px;background:linear-gradient(180deg,#c77a24,#6a3a12 70%,#2a1a0c)" role="img" aria-label="Photo of a sunset behind a silhouetted tree"></div>
<p class="story-copy abs" style="left:133px">Ut ut tellus augue, ut rhoncus massa. Donec nisl nulla, molestie a semper in, luctus ac nunc. Cras eget nibh eu eros sollicitudin imperdiet. Vestibulum ipsum odio, faucibus a semper eget, ultrices a velit. Proin a lorem et justo pellentesque pellen-</p>
<a class="button btn-read abs" style="left:272px;top:639px">read more</a>

<h3 class="story-title heading abs" style="left:358px">Description</h3>
<div class="story-thumb abs" style="left:359px;background:linear-gradient(180deg,#9fb6d8,#dfe6ef 45%,#6a8458 60%,#a9b9c9)" role="img" aria-label="Photo of a wooden pier on a calm lake"></div>
<p class="story-copy abs" style="left:452px">Ut ut tellus augue, ut rhoncus massa. Donec nisl nulla, molestie a semper in, luctus ac nunc. Cras eget nibh eu eros sollicitudin imperdiet. Vestibulum ipsum odio, faucibus a semper eget, ultrices a velit. Proin a lorem et justo pellentesque pellen-</p>
<a class="button btn-read abs" style="left:590px;top:639px">read more</a>

<h3 class="session-title heading abs">Title of the session</h3>
<p class="session-copy abs">Sed semper sagittis ligula, ac convallis dolor lobortis vel. Aenean lacinia, sem non volutpat fermentum, sem enim venenatis turpis, vitae dapibus sem erat vehicula dolor. Donec eget felis ut lacus adipiscing sodales eget mattis lacus.</p>
<a class="button btn-read abs" style="left:38px;top:843px">read more</a>

<div class="gallery-image abs" style="left:237px;top:710px;background:linear-gradient(135deg,#f2b79f,#e9a58a)" role="img" aria-label="Pale world map on a salmon background"></div>
<p class="gallery-caption abs" style="left:237px;top:818px">Description Image</p>
<div class="gallery-image abs" style="left:463px;top:710px;background:linear-gradient(180deg,#4f86c4,#d9e3ee 45%,#5d7f9c 70%,#6b6a5c)" role="img" aria-label="Photo of a cable-stayed bridge over a harbour"></div>
<p class="gallery-caption abs" style="left:463px;top:818px">Description Image</p>
<div class="gallery-image abs" style="left:237px;top:859px;background:linear-gradient(135deg,#c4b38a,#a8956a)" role="img" aria-label="Antique parchment world map"></div>
<p class="gallery-caption abs" style="left:237px;top:967px">Description Image</p>
<div class="gallery-image abs" style="left:463px;top:859px;background:linear-gradient(120deg,#bcbfc2 0%,#7b8287 45%,#35b1d8 60%,#1b8fc0 100%)" role="img" aria-label="Three-dimensional blue relief map of a coastline"></div>
<p class="gallery-caption abs" style="left:463px;top:967px">Description Image</p>

<footer class="site-footer abs"></footer>
<div class="footer-col divider abs" style="left:40px;width:128px;padding-right:24px">
  <h4>Pages</h4>
  <ul class="page-links">
    <li>Home Page</li><li>About us</li><li>Technology</li><li>Research</li><li>Contact</li>
  </ul>
</div>
<div class="footer-col divider abs" style="left:200px;width:127px">
  <h4>Last updates</h4>
  <ul class="bullets">
    <li style="margin-bottom:6px">In hac habitasse platea dictumst. Praesent iaculis</li>
    <li>Faucibus pretium. Nullam dictum viverra augue id</li>
  </ul>
</div>
<div class="footer-col divider abs" style="left:360px;width:127px">
  <h4 style="line-height:14px">Contact<br>information</h4>
  <p class="contact">Our telephones:<br>540318227<br>540319446<br>Our email:<br>desk@landmarkatlas.org</p>
</div>
<div class="footer-col abs" style="left:520px;width:140px">
  <h4>Our affiliates</h4>
  <ul class="bullets">
    <li>Lorem ipsum dolor</li><li>Egestas diam</li><li>Aliquet Hendrerit</li><li>Libero et sudis</li><li>Non potest augue</li><li>Vehicula tempus porta</li>
  </ul>
</div>
<div class="footer-brand abs">
  <div class="name">Civic Landmark Atlas</div>
  <div class="rights">all rights reserved.</div>
</div>

</body>
</html>
```